Business Card Design

I would like a new business card that incorporates the new colors and font of the attached MDP4x10.pdf file of our new sign (latte & luxurious red from Halcott Brennan colors) with the logo from the old business card (file name is New2014.pdf). You can remove the phrases from the old card, and just use the contact info provided above. Please let me know if you have any questions.

Industry/Entity Type

Business

Contact Information for Business Card

Marcus Dean Pryor, LLC
Real Estate Attorney
482 Alder Street
Pine Hollow, GA 30588
(O) 555-302-4187
(C) 555-719-2630
marcus@mdpcounsel.com
mdpcounsel.com

```html
<!DOCTYPE html>
<html lang="en">
<head>
<meta charset="utf-8">
<title>Marcus Dean Pryor, LLC — Business Card</title>
<link rel="stylesheet" href="https://fonts.googleapis.com/css2?family=Source+Sans+3:wght@400;600&display=swap">
<style>
  :root {
    --page-bg: #e8e4df;
    --card-bg: #f6f4f2;
    --card-edge: #ffffff;
    --brand-red: #9b2335;
    --ink: #1f1f1f;
  }
  * { margin: 0; padding: 0; box-sizing: border-box; }
  html, body {
    width: 1200px; height: 900px; overflow: hidden;
    background: var(--page-bg);
    font-family: "Source Sans 3", "Myriad Pro", Arial, sans-serif;
  }
  .card {
    position: absolute; left: 112px; top: 151px;
    width: 975px; height: 597px;
    background: var(--card-bg);
    border: 4px solid var(--card-edge);
    border-radius: 22px;
    box-shadow: 0 10px 30px rgba(0,0,0,0.08);
  }
  .identity { position: absolute; left: 42px; top: 44px; }
  .identity .firm {
    color: var(--brand-red); font-weight: 600; font-size: 33px; line-height: 1.1;
  }
  .identity .role {
    color: var(--ink); font-size: 27px; line-height: 1.2; margin-top: 2px;
  }
  .identity .address {
    color: var(--ink); font-size: 27px; line-height: 1.35; margin-top: 14px;
    font-style: normal; padding-left: 3px;
  }
  .contacts {
    position: absolute; right: 52px; top: 54px;
    list-style: none; text-align: right;
  }
  .contacts li {
    display: flex; align-items: center; justify-content: flex-end;
    gap: 16px; height: 40.5px;
    color: var(--ink); font-size: 26px;
  }
  .contacts svg { width: 20px; height: 20px; flex: none; fill: var(--brand-red); }
  .brand-mark {
    position: absolute; left: 0; right: 0; top: 370px;
    text-align: center;
    color: var(--brand-red); font-weight: 600; font-size: 54px; line-height: 1.1;
  }
</style>
</head>
<body>
  <section class="card" aria-label="Business card">
    <header class="identity">
      <h1 class="firm">Marcus Dean Pryor, LLC</h1>
      <p class="role">Real Estate Attorney</p>
      <address class="address">482 Alder Street<br>Pine Hollow, GA 30588</address>
    </header>

    <ul class="contacts">
      <li>555-302-4187
        <svg viewBox="0 0 24 24" aria-hidden="true"><path d="M6.6 10.8a15 15 0 0 0 6.6 6.6l2.2-2.2a1 1 0 0 1 1-.25 11 11 0 0 0 3.6.6 1 1 0 0 1 1 1V20a1 1 0 0 1-1 1A17 17 0 0 1 3 4a1 1 0 0 1 1-1h3.5a1 1 0 0 1 1 1 11 11 0 0 0 .6 3.6 1 1 0 0 1-.25 1z"/></svg>
      </li>
      <li>555-719-2630
        <svg viewBox="0 0 24 24" aria-hidden="true"><path d="M7 2h10a2 2 0 0 1 2 2v16a2 2 0 0 1-2 2H7a2 2 0 0 1-2-2V4a2 2 0 0 1 2-2zm0 3v13h10V5zm5 14.2a1 1 0 1 0 0 2 1 1 0 0 0 0-2z"/></svg>
      </li>
      <li>marcus@mdpcounsel.com
        <svg viewBox="0 0 24 24" aria-hidden="true"><path d="M2 5h20v14H2zm2 2v.5l8 5 8-5V7zm0 3v7h16v-7l-8 5z"/></svg>
      </li>
      <li>www.mdpcounsel.com
        <svg viewBox="0 0 24 24" aria-hidden="true"><path d="M10.6 13.4a1 1 0 0 1 0-1.4l3.5-3.5a1 1 0 1 1 1.4 1.4L12 13.4a1 1 0 0 1-1.4 0zM8.5 20a4.5 4.5 0 0 1-3.2-7.7l2.5-2.5 1.4 1.4-2.5 2.5a2.5 2.5 0 0 0 3.6 3.6l2.5-2.5 1.4 1.4-2.5 2.5A4.5 4.5 0 0 1 8.5 20zm8.3-6.4-1.4-1.4 2.5-2.5a2.5 2.5 0 0 0-3.6-3.6l-2.5 2.5-1.4-1.4 2.5-2.5a4.5 4.5 0 0 1 6.4 6.4z"/></svg>
      </li>
    </ul>

    <p class="brand-mark">Marcus Dean Pryor</p>
  </section>
</body>
</html>
```